New web page design for our brand Casa Lunares

We have changed our logo and the image of our products, so we would like to redesign ,our web page as well according to the new design.
Our cosmetic products are based in nature and tradition, like they used to be prepared in the old pharmacies.
Our actual web is www.casalunaresweb.es, so we need similar estructure but completely different design.

Industry/Entity Type

Cosmetics

Number of Pages Required

5+ page

Requirements
Must have
• References to natural ingredients and also to old pharmacys or apothecaries.
Nice to have
• Nature images or old botanics drawings
• I would like to have a cover page with just an image saying welcome to Casa Lunares's world

```html
<!DOCTYPE html>
<html lang="en">
<head>
<meta charset="utf-8">
<title>Casa Lunares</title>
<link href="https://fonts.googleapis.com/css2?family=Open+Sans:wght@300;400;600;700&family=Noto+Serif:ital,wght@0,400;0,700;1,400&display=swap" rel="stylesheet">
<style>
:root{
  --page:#f7f6ee;
  --card:#fbfaf4;
  --panel:#efeee6;
  --ink:#3a302a;
  --muted:#7a7068;
  --brown:#3b2a22;
  --btn:#2e2620;
  --nav:#e9e6dc;
  --nav-line:#c9c2b2;
  --contact:#a1937a;
  --contact-light:#b4a78e;
  --footer:#8f8169;
  --white:#ffffff;
}
*{margin:0;padding:0;box-sizing:border-box}
html,body{width:1200px;height:3464px;overflow:hidden}
body{background:var(--page);color:var(--ink);font-family:"Noto Serif",Georgia,serif}

/* header */
.site-header{height:190px;position:relative;background:var(--page)}
.brand{position:absolute;left:0;right:0;top:44px;text-align:center;font-family:"Open Sans",Arial,sans-serif;font-weight:700;font-size:30px;letter-spacing:3px;color:var(--brown);text-transform:uppercase}
.brand-dot{display:inline-block;width:12px;height:12px;border-radius:50%;background:var(--brown);margin-right:12px;vertical-align:middle;position:relative;top:-3px}
.main-nav{position:absolute;left:200px;width:800px;top:140px;height:44px;background:var(--nav);border-top:1px solid var(--nav-line);border-bottom:1px solid var(--nav-line);display:flex;justify-content:center;align-items:center}
.main-nav a{font-family:"Open Sans",Arial,sans-serif;font-size:13px;font-weight:600;color:var(--ink);text-decoration:none;padding:0 13px;border-right:1px solid var(--nav-line);line-height:16px}
.main-nav a:last-child{border-right:none}
.main-nav a.active{color:var(--white);background:var(--brown);padding:14px 16px}

/* hero */
.hero{height:550px;position:relative;overflow:hidden;
  background:
    radial-gradient(ellipse 140px 180px at 6% 62%,rgba(255,255,255,.75),transparent 70%),
    radial-gradient(ellipse 120px 150px at 17% 78%,rgba(245,240,226,.8),transparent 70%),
    radial-gradient(ellipse 110px 120px at 30% 85%,rgba(228,200,120,.65),transparent 70%),
    radial-gradient(ellipse 130px 130px at 45% 88%,rgba(120,140,70,.45),transparent 70%),
    radial-gradient(ellipse 120px 140px at 62% 78%,rgba(226,140,50,.6),transparent 70%),
    radial-gradient(ellipse 110px 160px at 76% 70%,rgba(214,120,40,.55),transparent 70%),
    radial-gradient(ellipse 140px 200px at 92% 60%,rgba(255,252,244,.8),transparent 70%),
    radial-gradient(ellipse 700px 260px at 50% 20%,rgba(248,238,214,.9),transparent 75%),
    linear-gradient(180deg,#d8c49c 0%,#e6d4ae 45%,#c9a878 100%);}
.hero-shelf{position:absolute;left:0;right:0;bottom:0;height:70px;background:linear-gradient(180deg,rgba(160,120,70,0),rgba(140,100,60,.35))}
.hero-name{position:absolute;left:420px;top:60px;width:360px;height:120px;background:rgba(251,248,238,.88);border:2px solid rgba(59,42,34,.35);outline:1px solid rgba(251,248,238,.9);outline-offset:5px;display:flex;align-items:center;justify-content:center;font-family:"Open Sans",Arial,sans-serif;font-weight:700;font-size:32px;letter-spacing:2px;color:var(--brown);text-transform:uppercase}

/* section titles */
.section-title{font-family:"Open Sans",Arial,sans-serif;font-weight:600;font-size:28px;letter-spacing:2px;text-align:center;color:var(--ink);text-transform:uppercase}
.section-rule{width:60px;height:2px;background:var(--brown);margin:14px auto 0}
.section-sub{font-size:14px;font-style:italic;color:var(--muted);text-align:center;margin-top:22px}

/* welcome */
.welcome{height:600px;padding-top:40px}
.welcome-text{width:880px;margin:26px auto 0;font-size:14px;line-height:24px;text-align:center;color:var(--muted);font-style:italic}
.feature-row{width:960px;margin:50px auto 0;display:flex;gap:30px}
.feature-card{width:300px;height:300px;background:var(--card);box-shadow:0 2px 6px rgba(0,0,0,.12);text-align:center}
.feature-icon{width:56px;height:56px;border-radius:50%;background:var(--brown);margin:-14px auto 0;display:flex;align-items:center;justify-content:center}
.feature-title{font-family:"Open Sans",Arial,sans-serif;font-size:16px;font-weight:600;text-transform:uppercase;letter-spacing:1px;margin-top:10px}
.feature-image{height:90px;margin-top:12px}
.feature-text{font-size:11px;line-height:17px;color:var(--muted);padding:12px 22px 0}
.read-more{display:inline-block;margin-top:12px;background:var(--btn);color:var(--white);font-family:"Open Sans",Arial,sans-serif;font-size:10px;font-weight:600;padding:5px 12px}

/* procedures */
.procedures{height:680px;padding-top:80px;border-top:1px solid #e4e1d6}
.procedure-row{width:960px;margin:70px auto 0;display:flex;gap:30px}
.procedure-card{width:300px;height:340px;background:var(--panel);text-align:center;margin-top:50px}
.procedure-photo{width:150px;height:150px;border-radius:50%;margin:-50px auto 0;border:5px solid var(--white)}
.procedure-title{font-family:"Open Sans",Arial,sans-serif;font-size:17px;font-weight:600;text-transform:uppercase;letter-spacing:1px;margin-top:20px}
.procedure-text{font-size:11px;line-height:17px;color:var(--muted);padding:12px 26px 0}

/* gallery */
.gallery{height:680px;padding-top:40px}
.gallery-grid{margin-top:70px;display:grid;grid-template-columns:repeat(4,300px);grid-template-rows:220px 220px}
.gallery-grid div{position:relative}

/* testimonial */
.testimonial{height:280px;position:relative;text-align:center}
.quote{width:860px;margin:20px auto 0;font-size:13px;line-height:21px;font-style:italic;color:var(--muted)}
.quote-mark{font-family:"Open Sans",Arial,sans-serif;font-weight:700;font-size:22px;color:var(--brown);vertical-align:-4px}
.testimonial-nav{position:absolute;left:0;right:0;top:130px;display:flex;justify-content:center;align-items:center;gap:24px}
.avatar{width:120px;height:120px;border-radius:50%;background:radial-gradient(circle at 50% 40%,#d7b9a0,#8a6a55);border:4px solid var(--white);box-shadow:0 1px 4px rgba(0,0,0,.2)}

/* contact */
.contact{height:460px;background:var(--contact)}
.contact-head{height:60px;background:var(--contact-light);display:flex;align-items:center;justify-content:center;font-family:"Open Sans",Arial,sans-serif;font-weight:700;font-size:16px;letter-spacing:2px;color:var(--brown);text-transform:uppercase}
.contact-tabs{display:flex;justify-content:center;gap:110px;margin-top:36px;font-family:"Open Sans",Arial,sans-serif;font-size:14px;color:var(--brown)}
.contact-tabs span{padding-bottom:6px}
.contact-tabs .active{border-bottom:2px solid var(--brown)}
.contact-items{display:flex;justify-content:center;gap:128px;margin-top:60px}
.contact-item{width:200px;text-align:center}
.contact-icon{width:110px;height:110px;border-radius:50%;background:var(--brown);margin:0 auto;display:flex;align-items:center;justify-content:center;border:4px solid #cbbfa6}
.contact-label{font-family:"Open Sans",Arial,sans-serif;font-weight:700;font-size:18px;letter-spacing:1px;color:var(--brown);margin-top:18px;text-transform:uppercase}
.contact-value{font-size:11px;color:var(--brown);margin-top:6px}

.site-footer{height:24px;background:var(--footer);font-family:"Open Sans",Arial,sans-serif;font-size:10px;color:#efe8da;display:flex;align-items:center;justify-content:center}
</style>
</head>
<body>

<header class="site-header">
  <div class="brand"><span class="brand-dot"></span>Casa Lunares</div>
  <nav class="main-nav">
    <a class="active">HOME</a>
    <a>ABOUT US</a>
    <a>RESERVATION</a>
    <a>PROCEDURES</a>
    <a>BLOGS</a>
    <a>GALLERY</a>
    <a>SHOPCODES</a>
    <a>SHOP</a>
    <a>LOCATION</a>
  </nav>
</header>

<section class="hero" role="img" aria-label="Apothecary shelf with jars, tubes and bottles of natural cosmetic products on a warm aged background">
  <div class="hero-shelf"></div>
  <div class="hero-name">Casa Lunares</div>
</section>

<section class="welcome">
  <h2 class="section-title">A Warm Welcome</h2>
  <div class="section-rule"></div>
  <p class="welcome-text">Casa Lunares was born from the craft of the old village apothecary, where every remedy was mixed by hand. We keep that spirit alive with gentle formulas made from plants, oils and flowers, prepared slowly and with care, so each product brings a little of that tradition into your home.</p>
  <div class="feature-row">
    <article class="feature-card">
      <div class="feature-icon"><svg width="28" height="28" viewBox="0 0 28 28"><path d="M5 22 C5 10 14 5 23 5 C23 15 17 23 5 22 Z M5 22 L16 11" fill="none" stroke="#fff" stroke-width="2"/></svg></div>
      <h3 class="feature-title">Natural Care</h3>
      <div class="feature-image" role="img" aria-label="Natural care product bottles" style="background:radial-gradient(ellipse 50px 40px at 30% 60%,rgba(255,255,255,.9),transparent 70%),radial-gradient(ellipse 50px 40px at 70% 55%,rgba(230,210,150,.7),transparent 70%),linear-gradient(90deg,#c9d6e8,#eef1f4,#b8c8dc)"></div>
      <p class="feature-text">Our Natural Care line uses old recipes of herbs and oils to keep your skin soft and calm every day.</p>
      <span class="read-more">Read More</span>
    </article>
    <article class="feature-card">
      <div class="feature-icon"><svg width="28" height="28" viewBox="0 0 28 28"><circle cx="14" cy="14" r="8" fill="none" stroke="#fff" stroke-width="2"/><circle cx="14" cy="14" r="3" fill="#fff"/></svg></div>
      <h3 class="feature-title">Body Treatment</h3>
      <div class="feature-image" role="img" aria-label="Body treatment creams and tubes" style="background:radial-gradient(ellipse 50px 40px at 35% 60%,rgba(214,170,110,.6),transparent 70%),radial-gradient(ellipse 50px 40px at 65% 55%,rgba(255,255,255,.9),transparent 70%),linear-gradient(90deg,#efe6d2,#f8f4ea,#e3d6bc)"></div>
      <p class="feature-text">Creams and gels from the Body Treatment line are made with pure botanical extracts for the whole body.</p>
      <span class="read-more">Read More</span>
    </article>
    <article class="feature-card">
      <div class="feature-icon"><svg width="28" height="28" viewBox="0 0 28 28"><path d="M14 23 C4 16 4 8 9 7 C12 6 14 9 14 10 C14 9 16 6 19 7 C24 8 24 16 14 23 Z" fill="none" stroke="#fff" stroke-width="2"/></svg></div>
      <h3 class="feature-title">Family Health</h3>
      <div class="feature-image" role="img" aria-label="Family health soaps and balms" style="background:radial-gradient(ellipse 50px 40px at 30% 55%,rgba(200,190,120,.6),transparent 70%),radial-gradient(ellipse 50px 40px at 70% 60%,rgba(255,255,255,.9),transparent 70%),linear-gradient(90deg,#e9e2c6,#f5f1e2,#ddd3b0)"></div>
      <p class="feature-text">The Family Health range offers mild balms and soaps for all ages, just as the old pharmacy did.</p>
      <span class="read-more">Read More</span>
    </article>
  </div>
</section>

<section class="procedures">
  <h2 class="section-title">Popular Procedures</h2>
  <div class="section-rule"></div>
  <p class="section-sub">These procedures are the most loved by our visitors.</p>
  <div class="procedure-row">
    <article class="procedure-card">
      <div class="procedure-photo" role="img" aria-label="Aromatherapy foot treatment with flowers" style="background:radial-gradient(circle at 35% 40%,#f6dccb,#e0a98e 55%,#b9806a)"></div>
      <h3 class="procedure-title">Aromatheraphy</h3>
      <p class="procedure-text">A calm ritual with essential oils of lavender and rosemary to relax the mind and ease tension.</p>
      <span class="read-more">Read More</span>
    </article>
    <article class="procedure-card">
      <div class="procedure-photo" role="img" aria-label="Skin care massage treatment" style="background:radial-gradient(circle at 40% 45%,#e0b498,#9a6448 55%,#4e2e22)"></div>
      <h3 class="procedure-title">Skin Care</h3>
      <p class="procedure-text">Deep cleansing and gentle masks made from clay, honey and herbs to renew and brighten the skin.</p>
      <span class="read-more">Read More</span>
    </article>
    <article class="procedure-card">
      <div class="procedure-photo" role="img" aria-label="Herbal spa bowls with green leaves" style="background:radial-gradient(circle at 50% 55%,#e8dcc0,#9fb56e 45%,#3f5424)"></div>
      <h3 class="procedure-title">Herbal Spa</h3>
      <p class="procedure-text">Warm herbal compresses and baths with chamomile and mint that restore balance to body and spirit.</p>
      <span class="read-more">Read More</span>
    </article>
  </div>
</section>

<section class="gallery">
  <h2 class="section-title">Our Gallery</h2>
  <div class="section-rule"></div>
  <p class="section-sub">Take a look at our products and moments of wellbeing.</p>
  <div class="gallery-grid">
    <div role="img" aria-label="Candle and pink orchids" style="background:radial-gradient(ellipse 90px 70px at 50% 62%,#fbf4e8,transparent 70%),radial-gradient(ellipse 120px 80px at 15% 20%,#e2a9bb,transparent 70%),linear-gradient(135deg,#ecc9d2,#b97d90)"></div>
    <div role="img" aria-label="Hot stone massage" style="background:radial-gradient(ellipse 160px 60px at 50% 70%,#e8c3a2,transparent 70%),radial-gradient(ellipse 60px 40px at 55% 30%,#3a3430,transparent 70%),linear-gradient(135deg,#d6ad8c,#7e553b)"></div>
    <div role="img" aria-label="Facial clay mask" style="background:radial-gradient(ellipse 90px 110px at 55% 50%,#5a534c,transparent 70%),radial-gradient(ellipse 80px 80px at 15% 85%,#e8d2b8,transparent 70%),linear-gradient(135deg,#aaa298,#4a443e)"></div>
    <div role="img" aria-label="Pedicure with daisies" style="background:radial-gradient(ellipse 130px 70px at 55% 45%,#f4d6c4,transparent 70%),radial-gradient(ellipse 50px 40px at 25% 75%,#ffffff,transparent 70%),linear-gradient(135deg,#efdccf,#c9977f)"></div>
    <div role="img" aria-label="Rolled white towels with flowers" style="background:radial-gradient(ellipse 120px 80px at 40% 55%,#ffffff,transparent 70%),radial-gradient(ellipse 50px 40px at 70% 75%,#e7a0b4,transparent 70%),linear-gradient(135deg,#eeeae0,#a99f8a)"></div>
    <div role="img" aria-label="Coconut bowl with spa salts" style="background:radial-gradient(ellipse 110px 60px at 50% 50%,#f0e6d2,transparent 70%),radial-gradient(ellipse 150px 90px at 50% 65%,#b07a40,transparent 75%),linear-gradient(135deg,#caa06a,#5c3c1c)"></div>
    <div role="img" aria-label="Hand massage with petals" style="background:radial-gradient(ellipse 130px 70px at 50% 55%,#f4cfc2,transparent 70%),radial-gradient(ellipse 50px 40px at 20% 25%,#e58fa0,transparent 70%),linear-gradient(135deg,#eec7bf,#a86e64)"></div>
    <div role="img" aria-label="Herbal bowls with flowers" style="background:radial-gradient(ellipse 80px 60px at 35% 55%,#f2ecd0,transparent 70%),radial-gradient(ellipse 80px 60px at 70% 45%,#c9c27a,transparent 70%),linear-gradient(135deg,#d9d2a0,#77763c)"></div>
  </div>
</section>

<section class="testimonial">
  <p class="quote"><span class="quote-mark">“</span> Their creams remind me of the remedies my grandmother kept in her cupboard. Everything smells of real plants and feels gentle on the skin. The staff explain every ingredient with patience, and I always leave feeling cared for and calm. <span class="quote-mark">”</span></p>
  <div class="testimonial-nav">
    <svg width="14" height="20" viewBox="0 0 14 20"><path d="M11 2 L3 10 L11 18" fill="none" stroke="#9a9088" stroke-width="2"/></svg>
    <div class="avatar" role="img" aria-label="Portrait of a customer"></div>
    <svg width="14" height="20" viewBox="0 0 14 20"><path d="M3 2 L11 10 L3 18" fill="none" stroke="#9a9088" stroke-width="2"/></svg>
  </div>
</section>

<section class="contact">
  <div class="contact-head">Contact Info</div>
  <div class="contact-tabs">
    <span class="active">Contact Info</span>
    <span>General Inquiry</span>
    <span>View on Map</span>
  </div>
  <div class="contact-items">
    <div class="contact-item">
      <div class="contact-icon"><svg width="40" height="40" viewBox="0 0 40 40"><path d="M20 36 C12 25 8 19 8 14 A12 12 0 0 1 32 14 C32 19 28 25 20 36 Z" fill="#fff"/><circle cx="20" cy="14" r="5" fill="#3b2a22"/></svg></div>
      <div class="contact-label">Address</div>
      <div class="contact-value">Calle del Olivo 12, 28013 Madrid</div>
    </div>
    <div class="contact-item">
      <div class="contact-icon"><svg width="40" height="40" viewBox="0 0 40 40"><path d="M10 6 L16 6 L18 14 L14 17 C16 22 18 24 23 26 L26 22 L34 24 L34 30 C34 32 32 34 30 34 C18 33 7 22 6 10 C6 8 8 6 10 6 Z" fill="#fff"/></svg></div>
      <div class="contact-label">Phones</div>
      <div class="contact-value">+34 910 000 000</div>
    </div>
    <div class="contact-item">
      <div class="contact-icon"><svg width="40" height="40" viewBox="0 0 40 40"><rect x="6" y="10" width="28" height="20" fill="#fff"/><path d="M6 10 L20 22 L34 10" fill="none" stroke="#3b2a22" stroke-width="2"/></svg></div>
      <div class="contact-label">E-Mail</div>
      <div class="contact-value">info@casalunaresweb.es</div>
    </div>
  </div>
</section>

<footer class="site-footer">Copyright © 2024 casalunaresweb.es All rights reserved</footer>

</body>
</html>
```